Business Card

The design you sent was fine. I just need the logo changed on one side. The back needs to have the text "Vela Norquist Group" next to the log and the words "Counsel Insight Support" in the middle. The front logo needs to have the "Vela Norquist Advisory" logo attached

Colors

Designer to choose colors to be used in the design.

```html
<!DOCTYPE html>
<html lang="en">
<head>
<meta charset="utf-8">
<title>Vela Norquist Business Card</title>
<link href="https://fonts.googleapis.com/css2?family=Open+Sans:wght@400;600;700&display=swap" rel="stylesheet">
<style>
  :root {
    --backdrop: #1d1d1e;
    --card: #ffffff;
    --card-shade: #f1f1f1;
    --ink: #1a1a1a;
    --accent: #1ab4e3;
    --rule: #3a3a3a;
  }
  * { box-sizing: border-box; margin: 0; padding: 0; }
  html, body { width: 1200px; height: 1021px; overflow: hidden; }
  body {
    background: var(--backdrop);
    font-family: "Open Sans", Arial, sans-serif;
    color: var(--ink);
    position: relative;
  }
  .card {
    position: absolute;
    left: 250px;
    width: 700px;
    height: 400px;
    background: linear-gradient(180deg, var(--card) 55%, var(--card-shade) 100%);
    box-shadow: 0 6px 18px rgba(0,0,0,0.45);
  }
  .card--back { top: 60px; }
  .card--front { top: 540px; }

  /* Back side */
  .brand-lockup {
    position: absolute;
    left: 140px;
    top: 150px;
    display: flex;
    align-items: center;
    gap: 24px;
  }
  .brand-circle {
    width: 64px; height: 64px;
    border-radius: 50%;
    background: var(--accent);
    flex: none;
  }
  .brand-text { display: flex; flex-direction: column; }
  .brand-name {
    font-size: 38px;
    font-weight: 600;
    line-height: 1.1;
    color: var(--ink);
  }
  .brand-tagline {
    margin-top: 4px;
    margin-left: 56px;
    font-size: 15px;
    font-weight: 400;
    letter-spacing: 1px;
    color: var(--ink);
  }

  /* Front side */
  .advisory-lockup {
    position: absolute;
    left: 38px;
    top: 115px;
    width: 290px;
  }
  .advisory-mark {
    display: flex;
    align-items: center;
    gap: 14px;
  }
  .advisory-circle {
    width: 52px; height: 52px;
    border-radius: 50%;
    background: var(--accent);
    flex: none;
  }
  .advisory-name {
    font-size: 24px;
    font-weight: 600;
    line-height: 1.15;
    color: var(--ink);
  }
  .advisory-tagline {
    margin-top: 12px;
    padding-top: 6px;
    border-top: 1px solid var(--ink);
    font-size: 8.5px;
    font-weight: 600;
    color: var(--ink);
    text-align: center;
  }
  .divider {
    position: absolute;
    left: 360px;
    top: 90px;
    width: 1px;
    height: 215px;
    background: var(--rule);
  }
  .contact {
    position: absolute;
    left: 385px;
    top: 92px;
    font-size: 16px;
    line-height: 1.35;
  }
  .contact__name {
    font-size: 22px;
    font-weight: 600;
    color: var(--accent);
  }
  .contact__title { font-size: 17px; margin-bottom: 16px; }
  .contact__address { margin-bottom: 6px; }
  .contact__row {
    display: flex;
    align-items: center;
    gap: 8px;
  }
  .contact__row svg { width: 14px; height: 14px; flex: none; }
</style>
</head>
<body>

  <section class="card card--back">
    <div class="brand-lockup">
      <div class="brand-circle"></div>
      <div class="brand-text">
        <div class="brand-name">Vela Norquist Group</div>
        <p class="brand-tagline">Counsel Insight Support</p>
      </div>
    </div>
  </section>

  <section class="card card--front">
    <div class="advisory-lockup">
      <div class="advisory-mark">
        <div class="advisory-circle"></div>
        <div class="advisory-name">Vela Norquist Advisory</div>
      </div>
      <p class="advisory-tagline">Careful Thinking delivering Practical Results</p>
    </div>

    <div class="divider"></div>

    <div class="contact">
      <p class="contact__name">Daniel Harlowe</p>
      <p class="contact__title">President</p>
      <p class="contact__address">48 Larkspur Row, Suite 310<br>Brightwater, Oregon, 97420</p>
      <p class="contact__row">
        <svg viewBox="0 0 16 16" aria-hidden="true"><path fill="#1ab4e3" d="M3.6 1.2l2.3 2.6-1.2 1.8c.9 2 2.6 3.7 4.6 4.6l1.8-1.2 2.6 2.3-1.4 2.3C7 13.4 2.6 9 1.4 2.6z"/></svg>
        (555) 210-4478
      </p>
      <p class="contact__row">
        <svg viewBox="0 0 16 16" aria-hidden="true"><rect x="1" y="3" width="14" height="10" fill="none" stroke="#1ab4e3" stroke-width="1.5"/><path d="M1 3l7 6 7-6" fill="none" stroke="#1ab4e3" stroke-width="1.5"/></svg>
        daniel@velanorquist-advisory.com
      </p>
      <p class="contact__row">
        <svg viewBox="0 0 16 16" aria-hidden="true"><g fill="none" stroke="#1ab4e3" stroke-width="1.3"><circle cx="8" cy="8" r="6.5"/><ellipse cx="8" cy="8" rx="3" ry="6.5"/><path d="M1.5 8h13M2.5 4.8h11M2.5 11.2h11"/></g></svg>
        www.velanorquist-advisory.com
      </p>
    </div>
  </section>

</body>
</html>
```